Hi
Thank you for considering my job.

I need a layout design for a website. The design should preferably suit GainsFrame Sitecraft layout. Please design according to the attached LAYOUT.GIF

I already have a logo which I like but could be pushed to change if you have an exceptional design. Otherwise I would like to try to incorporate the jigsaw pieces in the design somehow.

Our company is based in Australia and called Parting Toolbox. We have developed a "Apart Pack" to assist both men and women going through divorce to prepare themselves adequately before the seek legal or financial advice to ensure they pay professionals for "advice" and not instructions on basic administration.

I hope the successful candidate will also be able to design a logo and squeeze page and all of the marketing images I will need to accompany The Apart Pack in a few weeks time, though it is not part of this job.

I have attached a very rough guide as to the types of elements and how I would like it to feel. I am not set on any of the fonts or general presentation at all. I feel comfortable with the colour scheme but again, open to ideas. Although the logo has the dark teal green background, I am not sure this works on the web page - open to ideas.

Some must haves:
a video on the front page
an opt in/members' login
link to Tarvello books sales (affiliate widget)
Disclaimer must be visible on first SCREEN

The website must portray a professional, trustworthy and up to date type image - similar to a law firm, accounting firm, bank or university. It must be clean and crisp, inviting and non-gender biased.

Please message me if you have any questions at all.

Thanks again.
Marguerite
Perth, Australia

Target Market(s)

Australian MEN AND WOMEN - 30 - 60 years middle to upper income earners

Industry/Entity Type

Accounting

Requirements
Must have
• Some must haves:
a video on the front page
an opt in/members' login

The website must portray a professional, trustworthy and up to date type image - similar to a law firm, accounting firm BUT SLIGHTLY MORE PEOPLE ORIENTED

```html
<!DOCTYPE html>
<html lang="en">
<head>
<meta charset="utf-8">
<title>Parting Toolbox – clear guidance, one step at a time</title>
<link rel="stylesheet" href="https://fonts.googleapis.com/css2?family=Noto+Serif:ital,wght@0,400;1,400;1,700&family=Open+Sans:wght@300;400;600&display=swap">
<style>
:root{
  --teal-dark:#053f5a;
  --teal-line:#0c4a66;
  --orange:#f4694a;
  --cyan:#16c6e6;
  --cyan-soft:#17c4e2;
  --page-grey:#eeeeee;
  --panel:#ffffff;
  --text:#6a6a6a;
  --rule:#c9c9c9;
  --disclaimer-bg:#fde6df;
}
*{box-sizing:border-box;margin:0;padding:0}
html,body{width:1191px;height:1200px;overflow:hidden}
body{position:relative;background:linear-gradient(#eeeeee 0,#f6f6f6 700px,#ffffff 1100px);font-family:"Open Sans",Arial,sans-serif;color:var(--text)}
a{color:inherit;text-decoration:none}

/* header */
.site-header{position:absolute;left:0;top:0;width:1191px;height:134px;background:var(--teal-dark)}
.brand{position:absolute;left:79px;top:34px;display:flex;align-items:center;gap:16px}
.brand-mark{width:44px;height:44px;background:var(--cyan)}
.brand-name{font-family:"Open Sans",Arial,sans-serif;font-weight:400;font-size:40px;line-height:1;color:#fff}
.brand-tagline{position:absolute;left:139px;top:86px;font-family:"Open Sans",Arial,sans-serif;font-size:17px;color:#fff}
.login{position:absolute;left:890px;top:29px;width:260px}
.login-fields{display:flex;gap:2px}
.login-input{width:93px;height:21px;background:#fff;border:0}
.login-button{margin-left:6px;width:61px;height:21px;background:var(--cyan);color:var(--teal-dark);font-size:12px;line-height:21px;text-align:center}
.login-options{margin-top:8px;font-size:11px;color:var(--cyan);display:flex;gap:10px;align-items:center}
.login-options .remember{color:#fff;display:flex;align-items:center;gap:3px}
.login-options .remember i{display:inline-block;width:8px;height:8px;background:#fff}
.register{margin-top:14px;font-size:11.5px;color:#d5e3ea}
.register a{color:var(--cyan)}
.register-note{font-size:10.5px;color:#fff;margin-top:2px}

/* nav */
.main-nav{position:absolute;left:0;top:134px;width:1191px;height:49px;background:var(--page-grey)}
.nav-list{position:absolute;left:76px;top:16px;display:flex;list-style:none;font-size:13px;color:var(--teal-dark)}
.nav-list li{margin-right:23px}
.search{position:absolute;left:986px;top:12px;width:94px;height:21px;background:#fff;font-size:11px;color:#555;padding:2px 6px}
.social{position:absolute;top:12px;width:22px;height:22px;background:var(--teal-line)}
.social.one{left:1096px}
.social.two{left:1127px;background:#2da7dc}

/* content panel */
.content{position:absolute;left:42px;top:183px;width:1107px;height:920px;background:var(--panel)}
.page-title{position:absolute;left:76px;top:201px;font-family:"Noto Serif",Georgia,serif;font-style:italic;font-weight:400;font-size:29px;color:var(--teal-dark)}

.intro{position:absolute;left:76px;top:254px;width:392px;height:280px;border:2px solid var(--teal-dark);padding:14px 18px}
.intro-head{font-family:"Noto Serif",Georgia,serif;font-style:italic;font-size:20.5px;line-height:26px;color:var(--orange)}
.intro-body{margin-top:14px;font-size:14.5px;font-weight:400;line-height:22px;color:var(--orange)}
.intro-more{position:absolute;left:18px;bottom:12px;font-size:15.5px;color:var(--teal-dark)}

.video{position:absolute;left:481px;top:254px;width:372px;height:280px;border:2px solid var(--teal-dark);background:#fff}
.video svg{position:absolute;left:160px;top:114px}

.articles{position:absolute;left:76px;top:547px;width:777px;height:443px;background:linear-gradient(#ececec,#fafafa 70%,#ffffff)}
.article{position:absolute;left:19px;width:720px}
.article-title{font-family:"Noto Serif",Georgia,serif;font-style:italic;font-weight:700;font-size:19px;color:var(--teal-dark);line-height:24px}
.article-date{font-family:"Noto Serif",Georgia,serif;font-style:italic;font-size:16px;color:var(--teal-dark);line-height:22px}
.article-text{font-size:14.5px;line-height:20px;font-weight:400;color:#666}
.article-text a{color:var(--teal-dark);font-weight:400}
.scrollbar{position:absolute;left:764px;top:0;width:13px;height:443px;background:#d4d4d4}
.scrollbar i{position:absolute;left:3px;top:122px;width:7px;height:52px;background:#f7f7f7}

.promo{position:absolute;top:1005px;height:68px;padding:12px 19px;font-size:19.5px;line-height:22px}
.promo.tool{left:76px;width:381px;background:var(--cyan);color:var(--teal-dark)}
.promo.tool b{font-weight:600}
.promo.tool small{display:block;font-size:13px;margin-top:3px}
.promo.space{left:472px;width:381px;background:var(--orange);color:var(--teal-dark)}
.promo.space b{font-weight:600}

/* sidebar */
.testimonial{position:absolute;left:889px;top:205px;width:225px;font-family:"Noto Serif",Georgia,serif;font-style:italic;font-size:20px;line-height:28px;color:var(--cyan-soft)}
.side-rule{position:absolute;left:889px;width:225px;height:1px;background:var(--rule)}
.join{position:absolute;left:889px;top:360px;width:230px}
.join h2{font-weight:300;font-size:21px;color:var(--teal-dark);margin-bottom:6px}
.join ul{list-style:none}
.join li{position:relative;padding-left:17px;font-size:13.5px;line-height:19px;color:var(--teal-dark);margin-bottom:9px}
.join li svg{position:absolute;left:0;top:3px}
.buy{position:absolute;left:889px;top:546px;font-family:"Noto Serif",Georgia,serif;font-style:italic;font-size:24px;color:var(--orange)}
.price{position:absolute;left:889px;top:578px;font-size:17px;font-weight:600;color:var(--orange)}
.book{position:absolute;left:889px;top:633px;width:225px;height:193px;background:linear-gradient(135deg,#2f6f7e,#0d4455 60%,#e8e8e8 61%,#cfcfcf)}
.book-text{position:absolute;left:889px;top:846px;width:225px;font-size:14px;line-height:20px;color:#666}
.book-text a{color:var(--teal-dark)}
.book-widget{position:absolute;left:889px;top:1006px;width:225px;height:64px;background:linear-gradient(90deg,#b9463a,#444 25%,#c8a24a 45%,#2c2c2c 60%,#8a3030 80%,#333)}

/* footer */
.disclaimer{position:absolute;left:186px;top:1148px;width:824px;height:19px;background:var(--disclaimer-bg);font-size:12px;line-height:19px;text-align:center;color:#555}
.footer-links{position:absolute;left:0;top:1180px;width:1191px;display:flex;justify-content:center;gap:27px;font-size:11.5px;color:var(--teal-dark);list-style:none}
</style>
</head>
<body>

<header class="site-header">
  <div class="brand"><span class="brand-mark"></span><span class="brand-name">partingtoolbox</span></div>
  <div class="brand-tagline">clear guidance, one step at a time</div>
  <form class="login">
    <div class="login-fields"><span class="login-input"></span><span class="login-input"></span><span class="login-button">LOG IN</span></div>
    <div class="login-options"><a href="#">FORGET LOGIN?</a><span class="remember"><i></i>REMEMBER</span></div>
    <p class="register">Not accout yet? <a href="#">REGISTER FOR FREE TODAY</a></p>
    <p class="register-note">Do not use your name as username</p>
  </form>
</header>

<nav class="main-nav">
  <ul class="nav-list">
    <li>HOME</li><li>CONSIDERING DIVORCE</li><li>LEGAL PROCESS</li><li>PARENTING</li><li>PROPERTY &amp; FINANCE</li><li>COMMUNITY</li><li>TOOLS</li><li>FAQS</li><li>BOOKS</li>
  </ul>
  <div class="search">Search</div>
  <span class="social one" role="img" aria-label="Social profile link"></span>
  <span class="social two" role="img" aria-label="Social profile link"></span>
</nav>

<main>
  <div class="content"></div>
  <h1 class="page-title">Click to play the Video Guide (image below)</h1>

  <section class="intro">
    <p class="intro-head">The Apart Pack Fake text. Thank for using Marks of the Globe your logo needs. This site is made possible thanks to contributions</p>
    <p class="intro-body">From people like you who upload vector logos for designers, so we can reproduce brands oln artworkscorrectly and with high quality. Please consider uploading any vector logos that.</p>
    <a class="intro-more" href="#">CLICK TO LEARN MORE</a>
  </section>

  <section class="video" aria-label="Video guide">
    <svg width="52" height="52" viewBox="0 0 52 52"><circle cx="26" cy="26" r="26" fill="#053f5a"/><path d="M20 14 L38 26 L20 38 Z" fill="#fff"/></svg>
  </section>

  <section class="articles">
    <article class="article" style="top:16px">
      <h3 class="article-title">Article 04 (title)</h3>
      <p class="article-date">Apr. 2013</p>
      <p class="article-text">This site is made possible thanks to contributions frm people like you who uploadontributions from people like you who upload This site is&nbsp; vector logos for designers, so we can... <a href="#">+ READ MORE</a></p>
    </article>
    <article class="article" style="top:126px">
      <h3 class="article-title">Article 03 (title)</h3>
      <p class="article-date">Mar. 2013</p>
      <p class="article-text">This site is made possible thanks to contributions frm people like you who uploadontributions from people like you who upload This site is&nbsp; vector logos for designerrmn... <a href="#">+ READ MORE</a></p>
    </article>
    <article class="article" style="top:236px">
      <h3 class="article-title">Article 02 (title)</h3>
      <p class="article-date">Feb. 2013</p>
      <p class="article-text">This site is made possible thanks to contributions frm people like you who uploadontributions from people like you who upload This site is&nbsp; vector logos for designers, so we can... <a href="#">+ READ MORE</a></p>
    </article>
    <article class="article" style="top:343px">
      <h3 class="article-title">Article 01 (title)</h3>
      <p class="article-date">Jan. 2013</p>
      <p class="article-text">This site is made possible thanks to contributions frm people like you who uploadontributions from people like you who upload This site is&nbsp; vectan... <a href="#">+ READ MORE</a></p>
    </article>
    <div class="scrollbar"><i></i></div>
  </section>

  <a class="promo tool" href="#">TRY OUR <b>FREE DIVORCE TOOL</b><small>From people you who upload.</small></a>
  <a class="promo space" href="#"><b>FREE SPACE</b> IN CASE<br>YOU NEED</a>
</main>

<aside>
  <p class="testimonial">“Testimonials in order to entice the person to stay on the website, testimonials...”</p>
  <div class="side-rule" style="top:338px"></div>
  <section class="join">
    <h2>JOIN OUR COMMUNITY</h2>
    <ul>
      <li><svg width="13" height="13" viewBox="0 0 13 13"><path d="M1 7 L5 11 L12 1" fill="none" stroke="#053f5a" stroke-width="2"/></svg>Free membership</li>
      <li><svg width="13" height="13" viewBox="0 0 13 13"><path d="M1 7 L5 11 L12 1" fill="none" stroke="#053f5a" stroke-width="2"/></svg>Instant free access&nbsp; to calculators and resources</li>
      <li><svg width="13" height="13" viewBox="0 0 13 13"><path d="M1 7 L5 11 L12 1" fill="none" stroke="#053f5a" stroke-width="2"/></svg>Anonymous participation in support and advice forums</li>
    </ul>
  </section>
  <div class="side-rule" style="top:532px"></div>
  <p class="buy">Buy Now!</p>
  <p class="price">$ 12.99</p>
  <div class="book" role="img" aria-label="Cover of the downloadable guide book, dark teal"></div>
  <p class="book-text">Download Immediately. This simple guide provides a wealth of essential information and answers to your questions. Advice and tips to help you get a grip on all the changes in your life. <a href="#">+ READ MORE</a></p>
  <div class="book-widget" role="img" aria-label="Tarvello book sales widget showing a row of book covers"></div>
</aside>

<footer>
  <p class="disclaimer">Disclaimer fake text Disclaimer fake text Disclaimer fake text Disclaimer fake text Disclaimer fake text Disclaimer fake text Disclaimer fake text</p>
  <ul class="footer-links"><li>ABOUT US</li><li>CONTACTS</li><li>PRIVACY POLICY</li><li>DISCLAIMER</li></ul>
</footer>

</body>
</html>
```